Service company standing banner design

We are an existing company that just updated our logo. We are attending some oportunity summits in the near future and want a new crisp clean look on our three banners that will be placed in the back of our small booth. The summits we are attending are designed to give local companies opportunities on a prokect we have been awarded to construct in their area. These banners should communicate who we are with no questions when people see them. One banner shall list our services. One to list our values and one to state our goals. All these while being appealing to the eye and using picture of nature. Attached are copies of what we are to replace. also the new logo and the original background pictures in the existing banners

```html
<!DOCTYPE html>
<html lang="en">
<head>
<meta charset="utf-8">
<title>Booth Banners</title>
<link href="https://fonts.googleapis.com/css2?family=Poppins:wght@300;500;600;700&family=Questrial&family=Oswald:wght@700&family=Baloo+2:wght@700&display=swap" rel="stylesheet">
<style>
  :root {
    --page: #f5f6f7;
    --ink: #1c1a16;
    --sky: #22a6e2;
    --sky-deep: #1483c9;
    --sky-pale: #d9f1fb;
    --orange: #f58a3c;
    --navy: #183a9c;
    --shadow: #86afd2;
    --white: #ffffff;
  }
  * { box-sizing: border-box; margin: 0; padding: 0; }
  html, body { width: 1200px; height: 1200px; overflow: hidden; }
  body { background: var(--page); font-family: "Poppins", sans-serif; position: relative; }

  .sheet-title {
    position: absolute; top: 28px; left: 0; width: 1200px; text-align: center;
    font-weight: 700; font-size: 32px; color: var(--ink);
  }
  .sheet-specs {
    position: absolute; top: 96px; left: 0; width: 1200px; text-align: center;
    font-weight: 500; font-size: 24px; color: var(--ink);
  }

  .banner {
    position: absolute; top: 248px; width: 346px; height: 816px;
    box-shadow: 10px 10px 0 var(--shadow);
    overflow: hidden; background: var(--white);
  }
  .banner--values { left: 54px; }
  .banner--services { left: 428px; }
  .banner--goals { left: 802px; }

  .photo { position: absolute; inset: 0; }
  .photo--river { background: linear-gradient(180deg, #1f2a22 0%, #26352b 40%, #3d5957 62%, #5d7a78 78%, #4b5a3e 100%); }
  .photo--snow { background: linear-gradient(180deg, #a9bcd6 0%, #c7d6e8 25%, #e3ebf3 50%, #f3f6fa 75%, #ffffff 100%); }
  .photo--mountain { background: linear-gradient(180deg, #596068 0%, #2d3a30 22%, #1e2a20 50%, #3f5a5a 75%, #6f8a8c 90%, #505a50 100%); }

  .shapes { position: absolute; inset: 0; width: 346px; height: 816px; }

  .values-list {
    position: absolute; top: 246px; left: 0; width: 346px; text-align: center;
    font-family: "Questrial", sans-serif; color: var(--white);
    font-size: 47px; line-height: 74px; list-style: none;
  }

  .services-heading {
    position: absolute; top: 80px; left: 0; width: 346px; text-align: center;
    font-family: "Oswald", sans-serif; font-weight: 700; font-size: 66px;
    letter-spacing: 6px; color: var(--orange); line-height: 80px;
    -webkit-text-stroke: 1.5px var(--white);
  }
  .services-list {
    position: absolute; top: 224px; left: 0; width: 346px; text-align: center;
    font-family: "Baloo 2", sans-serif; font-weight: 700; color: var(--navy);
    font-size: 27px; line-height: 49.6px; list-style: none;
  }

  .goals-kicker {
    position: absolute; top: 206px; left: 0; width: 346px; text-align: center;
    font-family: "Poppins", sans-serif; font-weight: 300; font-size: 21px; color: var(--white);
  }
  .goals-focus {
    position: absolute; top: 232px; left: 0; width: 346px; text-align: center;
    font-family: "Poppins", sans-serif; font-weight: 700; font-size: 27px;
    letter-spacing: 1px; color: var(--orange);
  }
  .goals-statement {
    position: absolute; top: 364px; left: 0; width: 346px; text-align: center;
    font-family: "Questrial", sans-serif; color: var(--white);
    font-size: 32px; line-height: 40px;
  }

  .brand {
    position: absolute; top: 706px; left: 0; width: 346px;
    display: flex; align-items: center; justify-content: center; gap: 10px;
  }
  .brand-mark { width: 46px; height: 46px; border-radius: 50%; background: var(--orange); flex: none; }
  .brand-name {
    font-family: "Poppins", sans-serif; font-weight: 600; font-size: 19px;
    line-height: 23px; color: var(--navy);
  }
</style>
</head>
<body>
  <h1 class="sheet-title">All Banners -</h1>
  <p class="sheet-specs">Deliverables: Ediatable: AI, PDF, EPS &nbsp;|&nbsp; Output Format: JPG, PNG, TIFF</p>

  <!-- Values banner -->
  <section class="banner banner--values">
    <div class="photo photo--river" role="img" aria-label="Photo of a forest-lined river flowing between rocky banks"></div>
    <svg class="shapes" viewBox="0 0 346 816" aria-hidden="true">
      <defs>
        <linearGradient id="capA" x1="0" y1="0" x2="1" y2="0">
          <stop offset="0" stop-color="#22a6e2"/><stop offset="0.7" stop-color="#7fcdec"/><stop offset="1" stop-color="#e4f5fb"/>
        </linearGradient>
        <linearGradient id="footA" x1="0" y1="0" x2="1" y2="0">
          <stop offset="0" stop-color="#35afe7"/><stop offset="0.5" stop-color="#bfe8f8"/><stop offset="1" stop-color="#ffffff"/>
        </linearGradient>
      </defs>
      <path d="M0,0 H322 C262,70 140,100 0,104 Z" fill="url(#capA)"/>
      <path d="M0,106 C140,102 262,72 322,0" fill="none" stroke="var(--orange)" stroke-width="6"/>
      <path d="M0,680 C120,690 282,644 346,584 V816 H0 Z" fill="var(--sky)"/>
      <path d="M0,702 C140,706 292,682 346,622 V816 H0 Z" fill="url(#footA)"/>
      <path d="M0,800 H346 V816 H0 Z" fill="var(--sky-deep)"/>
      <path d="M140,816 C170,804 230,804 260,816 Z" fill="#0f3552"/>
    </svg>
    <ul class="values-list">
      <li>Integrity</li><li>Transparency</li><li>Respect</li><li>Trust</li>
    </ul>
    <div class="brand"><span class="brand-mark"></span><span class="brand-name">Norvale Services<br>Limited Partnership</span></div>
  </section>

  <!-- Services banner -->
  <section class="banner banner--services">
    <div class="photo photo--snow" role="img" aria-label="Photo of snow-covered spruce trees in a winter forest"></div>
    <svg class="shapes" viewBox="0 0 346 816" aria-hidden="true">
      <defs>
        <linearGradient id="footB" x1="0" y1="0" x2="1" y2="0">
          <stop offset="0" stop-color="#ffffff"/><stop offset="0.5" stop-color="#bfe8f8"/><stop offset="1" stop-color="#35afe7"/>
        </linearGradient>
      </defs>
      <rect x="22" y="160" width="310" height="4" fill="var(--navy)"/>
      <path d="M0,576 C64,644 210,690 346,680 V816 H0 Z" fill="var(--sky)"/>
      <path d="M0,622 C60,684 206,706 346,702 V816 H0 Z" fill="url(#footB)"/>
      <path d="M0,800 H346 V816 H0 Z" fill="var(--sky-deep)"/>
      <path d="M90,816 C130,804 200,804 240,816 Z" fill="#0f3552"/>
    </svg>
    <h2 class="services-heading">SERVICES</h2>
    <ul class="services-list">
      <li>Pipeline Construction</li><li>Pipeline Clearing</li><li>Land Clearing</li><li>Civil Works</li>
      <li>Road Maintenance</li><li>Reclamation</li><li>Logging</li><li>Mulching</li>
    </ul>
    <div class="brand"><span class="brand-mark"></span><span class="brand-name">Norvale Services<br>Limited Partnership</span></div>
  </section>

  <!-- Goals banner -->
  <section class="banner banner--goals">
    <div class="photo photo--mountain" role="img" aria-label="Photo of a mountain valley with pine forest and a rushing river"></div>
    <svg class="shapes" viewBox="0 0 346 816" aria-hidden="true">
      <defs>
        <linearGradient id="capC" x1="0" y1="0" x2="1" y2="0">
          <stop offset="0" stop-color="#e4f5fb"/><stop offset="0.35" stop-color="#7fcdec"/><stop offset="1" stop-color="#22a6e2"/>
        </linearGradient>
        <linearGradient id="footC" x1="0" y1="0" x2="1" y2="0">
          <stop offset="0" stop-color="#35afe7"/><stop offset="0.5" stop-color="#bfe8f8"/><stop offset="1" stop-color="#ffffff"/>
        </linearGradient>
      </defs>
      <path d="M26,0 H346 V104 C206,100 86,70 26,0 Z" fill="url(#capC)"/>
      <path d="M26,0 C86,72 206,102 346,106" fill="none" stroke="var(--orange)" stroke-width="6"/>
      <path d="M0,680 C120,690 282,644 346,584 V816 H0 Z" fill="var(--sky)"/>
      <path d="M0,702 C140,706 292,682 346,622 V816 H0 Z" fill="url(#footC)"/>
      <path d="M0,800 H346 V816 H0 Z" fill="var(--sky-deep)"/>
      <path d="M140,816 C170,804 230,804 260,816 Z" fill="#0f3552"/>
    </svg>
    <p class="goals-kicker">Honouring the interests of</p>
    <p class="goals-focus">INDIGENOUS PEOPLE</p>
    <p class="goals-statement">To Build and Grow<br>a strong regional<br>business providing<br>the Best Quality for<br>our People and<br>Clients</p>
    <div class="brand"><span class="brand-mark"></span><span class="brand-name">Norvale Services<br>Limited Partnership</span></div>
  </section>
</body>
</html>
```